New, modern business card for growing audiology practice

We need a new business card for our audiology practice. Our logo and website have recently changed (more modern) and we want our business cards to reflect this change.
We conduct hearing tests, perform earwax removals, and fit & dispense hearing aids to our patients. We are a family owned practice in which the owner is the one who works directly with the patient. I have attached logos in various formats to use, as well as two ideas I found on this website; as well as a scanned copy of our current logo. Good luck!

Industry/Entity Type

Business

Contact Information for Business Card

Company name: Birchmont Hearing Center
Provider name: Peter Lowsby, Au.D. F/NSO
Phone number: (555) 318-6042
Address: 287 W. Hollister Rd. Larkmere Falls, OH 40000
email: birchmonthearing@quillpost.net
website: birchmonthearing.net

Colors
000000
aaaaaa
dbdbdb
cacaca
9bcb3c
afd23c
cadf82
b1b1b1

Requirements
Must have
• My card must include information in the "details" section. In the attached images, I found a few that I liked and I would like to model after - "steady strivin'" and "Sound Lab Clinic".
• Must be horizontal.
• Must include logos provided. I uploaded them in various file formats and various ways.
• Must match logo font, if possible, if not, please get as close as you can.
Nice to have
• I really like the idea of having a color on one side with just the logo and company name and the contact information and provider name on the other side. I also really like the idea of having the main color dominating on the logo/company side with accent of that same color on the contact side of the card.
Should not have
• Must not be vertical.

```html
<!DOCTYPE html>
<html lang="en">
<head>
<meta charset="utf-8">
<title>Birchmont Hearing Center – Business Card</title>
<link href="https://fonts.googleapis.com/css2?family=Lato:wght@300;400;700&display=swap" rel="stylesheet">
<style>
  :root {
    --canvas-bg: #2a2a2a;
    --card-bg: #1c1e1d;
    --card-edge: #111211;
    --brand-green: #9bcb3c;
    --text-light: #f2f2f2;
    --text-muted: #cacaca;
  }
  * { margin: 0; padding: 0; box-sizing: border-box; }
  html, body {
    width: 1200px; height: 1031px; overflow: hidden;
    background: var(--canvas-bg);
    font-family: 'Lato', sans-serif;
  }
  .canvas { position: relative; width: 1200px; height: 1031px; }
  .card { position: absolute; left: 260px; width: 680px; height: 340px; }
  .card--front { top: 110px; }
  .card--back { top: 581px; }
  .card-shape { position: absolute; inset: 0; }
  .card-shape path { fill: var(--card-bg); stroke: var(--card-edge); stroke-width: 2; }

  .brand { position: absolute; display: flex; align-items: center; gap: 14px; }
  .card--front .brand { left: 60px; top: 152px; }
  .brand-dot { width: 24px; height: 24px; border-radius: 50%; background: var(--brand-green); }
  .brand-name {
    color: var(--text-light); font-weight: 400; font-size: 32px;
    letter-spacing: 0.5px; text-transform: uppercase; white-space: nowrap;
  }

  .card--back .brand-name { position: absolute; left: 50px; top: 42px; font-size: 24px; }
  .provider { position: absolute; left: 50px; top: 100px; }
  .provider-name {
    color: var(--brand-green); font-weight: 700; font-size: 28px;
    text-transform: uppercase; letter-spacing: 0.5px;
  }
  .provider-title { color: var(--text-light); font-size: 20px; margin-top: 2px; }
  .contact-list { position: absolute; left: 50px; top: 190px; list-style: none; }
  .contact-item {
    display: flex; align-items: center; gap: 12px;
    color: var(--text-muted); font-size: 16px; line-height: 1; margin-bottom: 10px;
    white-space: nowrap;
  }
  .contact-icon { width: 18px; height: 18px; flex: none; }
  .contact-icon circle { fill: var(--brand-green); }
  .contact-icon .glyph { fill: none; stroke: var(--card-bg); stroke-width: 1.6; stroke-linecap: round; stroke-linejoin: round; }
</style>
</head>
<body>
<main class="canvas">

  <section class="card card--front" aria-label="Card front">
    <svg class="card-shape" viewBox="0 0 680 340" width="680" height="340">
      <path d="M20 0 H520 C560 0 575 20 600 40 C660 60 680 110 680 170 C680 230 660 280 600 300 C575 320 560 340 520 340 H20 Q0 340 0 320 V20 Q0 0 20 0 Z"/>
    </svg>
    <div class="brand">
      <span class="brand-dot"></span>
      <span class="brand-name">Birchmont Hearing Center</span>
    </div>
  </section>

  <section class="card card--back" aria-label="Card back">
    <svg class="card-shape" viewBox="0 0 680 340" width="680" height="340">
      <path d="M20 0 H520 C560 0 575 20 600 40 C660 60 680 110 680 170 C680 230 660 280 600 300 C575 320 560 340 520 340 H20 Q0 340 0 320 V20 Q0 0 20 0 Z"/>
    </svg>
    <span class="brand-name">Birchmont Hearing Center</span>
    <div class="provider">
      <div class="provider-name">Peter Lowsby</div>
      <div class="provider-title">Au.D. F/NSO</div>
    </div>
    <ul class="contact-list">
      <li class="contact-item">
        <svg class="contact-icon" viewBox="0 0 18 18"><circle cx="9" cy="9" r="9"/><path class="glyph" d="M6 5 L7.5 5 L8.3 7.2 L7.2 8 Q8 10 10 10.8 L10.8 9.7 L13 10.5 L13 12 Q10 13.5 7 10.8 Q4.5 8 6 5 Z"/></svg>
        (555) 318-6042
      </li>
      <li class="contact-item">
        <svg class="contact-icon" viewBox="0 0 18 18"><circle cx="9" cy="9" r="9"/><path class="glyph" d="M4.5 6 H13.5 V12.5 H4.5 Z M4.5 6 L9 9.8 L13.5 6"/></svg>
        birchmonthearing@quillpost.net
      </li>
      <li class="contact-item">
        <svg class="contact-icon" viewBox="0 0 18 18"><circle cx="9" cy="9" r="9"/><path class="glyph" d="M9 4.5 A4.5 4.5 0 1 0 9 13.5 A4.5 4.5 0 1 0 9 4.5 M4.5 9 H13.5 M9 4.5 Q6.5 9 9 13.5 M9 4.5 Q11.5 9 9 13.5"/></svg>
        www.birchmonthearing.net
      </li>
      <li class="contact-item">
        <svg class="contact-icon" viewBox="0 0 18 18"><circle cx="9" cy="9" r="9"/><path class="glyph" d="M9 14 Q5.5 10 5.5 7.8 A3.5 3.5 0 0 1 12.5 7.8 Q12.5 10 9 14 Z M9 6.6 A1.2 1.2 0 1 0 9 9 A1.2 1.2 0 1 0 9 6.6"/></svg>
        287 W. Hollister Rd. Larkmere Falls, OH 40000
      </li>
    </ul>
  </section>

</main>
</body>
</html>
```